verdant terraces simple classy business card design

my name is owen harlow and I run a gardening business aimed at high class verdant terraces. the business name is verdant terraces and our logo was designed on pixel forum .My clientel are anything from residential homes to businesses. I take pride in my work and know that I offer a service like no other in my area.
The business card will be used to represent my business and I want it to be not only rememberable, but simplistic and modern. Eye catching too. Of course I would like it relatable to gardening and appealing to the correct clientel - those being garden enthusiasts, prestigious homes and businesses that are after top of the line gardening services like no other on the market.
I am not a typical lawn mowing business so I don't want a typical card design that represents that. The gardens I work with are generally million dollar properties with owners who are very garden proud looking for upkeep and guidance from me along with sometimes whole new garden designs. I want the business cards to show to my clients that I take pride, as they do, in their garden. And I want them to know from my card that I am a professional, qualified horticulturist offering them a top of the line service for life. I want them to refer my business on. I want them to look at my business card and see class and professionalism in a modern unique bold way.
The card should be simple with the possibility of the logo on the front being embossed/debossed and my details on the back the card should have a organic garden feel it's very important to me that it is absolutely perfect
I am also very open to ideas and suggestions so look forward to seeing the designs. the business logo has been supplied with this project and I want the card to be double sided

Contact info is
Owen Harlow - Managing Director / Horticulturist
Phone : 0481 526 704
Email: owenharlow@verdantterraces.com.au

Target Market(s)

high class gardens residential and commercial

Industry/Entity Type

Gardener

Contact Information for Business Card

Contact info is
Phone : 0481 526 704

PLEASE MAKE CARD DOUBLE SIDED

Requirements
Must have
• organic simple classy modern feel
• must flow with the current logo that has been supplied with this project
• Double sided
• Must explain in a simple way that I deal with high end gardens and I'm a qualified horticulturist
Nice to have
• embossed debossed logo
Should not have
• shouldn't be to busy or cheap looking

```html
<!DOCTYPE html>
<html lang="en">
<head>
<meta charset="utf-8">
<title>Verdant Terraces – Business Card</title>
<link rel="stylesheet" href="https://fonts.googleapis.com/css2?family=Tinos:wght@400;700&display=swap">
<style>
  :root {
    --backdrop: #ece6dc;
    --card-paper: #f3f3f4;
    --card-fibre: rgba(180, 180, 190, 0.10);
    --leaf-green: #5f9b52;
    --leaf-green-deep: #4f8a44;
    --leaf-green-light: #b3d3aa;
    --ink: #2b2b2b;
    --white: #ffffff;
  }
  * { box-sizing: border-box; margin: 0; padding: 0; }
  html, body {
    width: 997px;
    height: 1200px;
    overflow: hidden;
    background: var(--backdrop);
  }
  .canvas {
    position: relative;
    width: 997px;
    height: 1200px;
  }
  .card {
    position: absolute;
    width: 777px;
    height: 462px;
    overflow: hidden;
    background-color: var(--card-paper);
    background-image:
      repeating-linear-gradient(90deg, var(--card-fibre) 0 1px, transparent 1px 4px),
      repeating-linear-gradient(0deg, rgba(255,255,255,0.35) 0 1px, transparent 1px 3px);
    box-shadow: 0 3px 10px rgba(0, 0, 0, 0.18);
    font-family: "Tinos", "Times New Roman", serif;
  }
  .card-front {
    left: 109px;
    top: 98px;
    border-radius: 8px 92px 8px 92px;
  }
  .card-back {
    left: 117px;
    top: 630px;
    border-radius: 92px 8px 92px 8px;
  }
  .card-band {
    position: absolute;
    inset: 0;
    width: 100%;
    height: 100%;
  }
  .band-fill { fill: var(--leaf-green); }
  .band-edge { fill: var(--leaf-green-light); }

  /* Front */
  .brand {
    position: absolute;
    left: 0;
    right: 0;
    top: 92px;
    display: flex;
    flex-direction: column;
    align-items: center;
    color: var(--leaf-green);
  }
  .brand-mark {
    width: 96px;
    height: 96px;
    border-radius: 50%;
    background: var(--leaf-green);
    margin-bottom: 30px;
  }
  .brand-name {
    font-family: "Tinos", "Times New Roman", serif;
    font-weight: 400;
    font-size: 44px;
    line-height: 1;
  }
  .role-tag {
    position: absolute;
    left: 0;
    right: 0;
    top: 392px;
    text-align: center;
    color: var(--white);
    font-size: 32px;
    letter-spacing: 0.5px;
  }

  /* Back */
  .foliage-art {
    position: absolute;
    left: 0;
    top: 30px;
    width: 200px;
    height: 330px;
    border-radius: 60% 45% 30% 0 / 45% 40% 35% 0;
    background: radial-gradient(ellipse at 55% 35%, var(--leaf-green) 0%, var(--leaf-green-deep) 100%);
  }
  .contact {
    position: absolute;
    left: 0;
    right: 0;
    top: 78px;
    text-align: center;
    color: var(--ink);
  }
  .contact-name {
    color: var(--leaf-green);
    font-weight: 700;
    font-size: 27px;
    line-height: 1;
  }
  .contact-title {
    font-size: 21px;
    line-height: 1;
    margin-top: 8px;
  }
  .contact-icon {
    display: block;
    margin: 0 auto;
  }
  .icon-phone { margin-top: 40px; }
  .contact-line {
    font-size: 23px;
    line-height: 1;
  }
  .contact-phone { margin-top: 20px; }
  .icon-mail { margin-top: 18px; }
  .contact-email { margin-top: 16px; }
  .web-tag {
    position: absolute;
    left: 0;
    right: 0;
    top: 389px;
    text-align: center;
    color: var(--white);
    font-weight: 700;
    font-size: 25px;
  }
</style>
</head>
<body>
<main class="canvas">

  <section class="card card-front" aria-label="Card front">
    <svg class="card-band" viewBox="0 0 777 462" preserveAspectRatio="none" aria-hidden="true">
      <path class="band-edge" d="M0,253 C0,322 40,345 125,345 L777,345 L777,462 L0,462 Z"/>
      <path class="band-fill" d="M0,263 C0,330 40,353 125,353 L777,353 L777,462 L0,462 Z"/>
    </svg>
    <div class="brand">
      <span class="brand-mark" aria-hidden="true"></span>
      <span class="brand-name">VERDANT TERRACES</span>
    </div>
    <p class="role-tag">HORTICULTURIST</p>
  </section>

  <section class="card card-back" aria-label="Card back">
    <div class="foliage-art" role="img" aria-label="Green leafy tree illustration rising from the lower left corner"></div>
    <svg class="card-band" viewBox="0 0 777 462" preserveAspectRatio="none" aria-hidden="true">
      <path class="band-edge" d="M777,245 C777,320 737,351 652,351 L0,351 L0,462 L777,462 Z"/>
      <path class="band-fill" d="M777,255 C777,330 737,359 652,359 L0,359 L0,462 L777,462 Z"/>
    </svg>
    <div class="contact">
      <p class="contact-name">OWEN HARLOW</p>
      <p class="contact-title">MANAGING DIRECTOR</p>
      <svg class="contact-icon icon-phone" width="18" height="30" viewBox="0 0 18 30" aria-hidden="true">
        <rect x="1.5" y="1.5" width="15" height="27" rx="2.5" fill="none" stroke="var(--leaf-green)" stroke-width="2.5"/>
        <rect x="4" y="5" width="10" height="17" fill="var(--leaf-green)" opacity="0.35"/>
        <circle cx="9" cy="25" r="1.4" fill="var(--leaf-green)"/>
      </svg>
      <p class="contact-line contact-phone">0481526704</p>
      <svg class="contact-icon icon-mail" width="30" height="20" viewBox="0 0 30 20" aria-hidden="true">
        <rect x="1.5" y="1.5" width="27" height="17" fill="none" stroke="var(--leaf-green)" stroke-width="2.2"/>
        <path d="M1.5,1.5 L15,12 L28.5,1.5 M1.5,18.5 L11,9.5 M28.5,18.5 L19,9.5" fill="none" stroke="var(--leaf-green)" stroke-width="2"/>
      </svg>
      <p class="contact-line contact-email">owenharlow@verdantterraces.com.au</p>
    </div>
    <p class="web-tag">www.verdantterraces.com.au</p>
  </section>

</main>
</body>
</html>
```